Book Cover Design Project

NOTE. I need the design in four days of posting this!

This will be the cover of my first book, WALK THE HIGH LINE -
PURPOSE IN THE MODERN WORKING WORLD. The book explains defines what Purpose and Meaning is, and how to use it in business. I have included the first chapter to provide a background.

I want the core colours to be black and white, and use the colours Violet, Cerulean Blue Extra Pale (powder blue), Cadmium Lemon (flouro yellow). I plan on using this design as the basis for future books in the WALK THE HIGH LINE series, where the yellow is carried through but the violet and blue colours changing.

This is a spiritual business book without using any spiritual language. It is strongly masculine and direct in its nature.

What I am looking for is something Remarkable that captures my reader immediately. My reader is a seeker. He/she is an entrepreneur perhaps looking to setup a new venture and looking for new and better ways of doing things, or he/she may be a small/medium business owner perhaps bored looking for more meaning in personal and business life), or the corporate person who is looking to get out and do something new. Age 35-50.
Updates

Hi I want to correct the paper size. It is "C Format" (trade paperbacks) are 135mm x 216mm (5.32" x 8.51").

Thks

Reason: A deadline has changed which means the completion of this book cover is less time-critical.

This is a business book that introduces new concepts, such as Purpose. Although it is based on spiritual principals  it is using normal business language when explaining what Purpose is, and how businesses can identify it and use it to be more successful.

If there is a border between a self-help and a business book, this book sits close to the border but markedly on the business side.

Hi I want to confirm the book size. The book size I require is the Australian C Format, which measures 153mm W x 234mm H. 

Sorry for any confusion

Reason: Hi I have extended the deadline as I want to be able to print prospective covers and see how they look like in a bookshop next to other covers.

Reason: To allow for final negotiations.

Industry/Entity Type

Business

```html
<!DOCTYPE html>
<html lang="en">
<head>
<meta charset="utf-8">
<title>Walk the High Line – Book Cover</title>
<link rel="stylesheet" href="https://fonts.googleapis.com/css2?family=Bebas+Neue&display=swap">
<style>
  :root {
    --page-bg: #e9eded;
    --cover-black: #121216;
    --cover-charcoal: #24242b;
    --title-white: #ffffff;
    --lemon: #f5ee0e;
    --subtitle-grey: #c9c9cf;
    --rule-white: #e6e6e6;
    --skyline-blue: #1d3a78;
    --skyline-violet: #2a2352;
  }
  * { margin: 0; padding: 0; box-sizing: border-box; }
  html, body {
    width: 1200px;
    height: 944px;
    overflow: hidden;
    background: var(--page-bg);
  }
  .cover {
    position: absolute;
    left: 332px;
    top: 62px;
    width: 536px;
    height: 820px;
    background:
      radial-gradient(ellipse at 45% 35%, var(--cover-charcoal) 0%, var(--cover-black) 75%);
    overflow: hidden;
    font-family: "Bebas Neue", "Oswald", sans-serif;
  }
  .title-block {
    position: absolute;
    left: 96px;
    top: 96px;
    right: 40px;
  }
  .title {
    font-weight: 400;
    line-height: 0.9;
    letter-spacing: 0.5px;
  }
  .title-line--white {
    display: block;
    color: var(--title-white);
    font-size: 104px;
  }
  .title-line--lemon {
    display: block;
    color: var(--lemon);
    font-size: 104px;
  }
  .title-rule {
    width: 330px;
    height: 3px;
    margin: 22px 0 0 -30px;
    background: var(--rule-white);
  }
  .subtitle {
    margin: 26px 0 0 -8px;
    color: var(--subtitle-grey);
    font-size: 34px;
    line-height: 1.05;
    font-weight: 400;
  }
  .subtitle-line { display: block; }
  .subtitle-line--first { color: var(--title-white); }
  .subtitle-accent { color: var(--lemon); }
  .author-name {
    position: absolute;
    left: 292px;
    top: 578px;
    color: var(--title-white);
    font-size: 26px;
    letter-spacing: 0.5px;
  }
  .skyline {
    position: absolute;
    left: 0;
    right: 0;
    bottom: 0;
    height: 230px;
    background: linear-gradient(
      to bottom,
      rgba(29, 58, 120, 0) 0%,
      rgba(29, 58, 120, 0.55) 45%,
      var(--skyline-violet) 100%
    );
  }
</style>
</head>
<body>
  <main class="cover">
    <div class="title-block">
      <h1 class="title">
        <span class="title-line--white">Walk the</span>
        <span class="title-line--lemon">High Line</span>
      </h1>
      <div class="title-rule"></div>
      <p class="subtitle">
        <span class="subtitle-line subtitle-line--first">Purpose in the <span class="subtitle-accent">Modern</span></span>
        <span class="subtitle-line">Working World</span>
      </p>
    </div>
    <p class="author-name">Author Name</p>
    <div class="skyline" role="img" aria-label="Blue city skyline silhouette along the bottom of the cover"></div>
  </main>
</body>
</html>
```